Junior Rugby Event needs 4 page Brochure

4 Page A4 brochure to be designed for a junior rugby event to be held in japan.. The brochure will entice coaches, teachers and players to the event.
The brochure will provide a basic overview of the event - dates, venue and promote some of the key features of the host, venue and event.
Event logo has been included. Design overview with copy has been included as word document. Images have been attached that can be used or alternatives sourced. A PDF document has been included of a design example that we like.
Target Market(s)
Rugby Clubs and Schools
Industry/Entity Type
Events
Look and feel

```html
<!DOCTYPE html>
<html lang="en">
<head>
<meta charset="utf-8">
<title>Pacific Youth Rugby Cup – Brochure Spread</title>
<link href="https://fonts.googleapis.com/css2?family=Archivo+Black&family=Oswald:wght@500&display=swap" rel="stylesheet">
<style>
  :root {
    --stage: #e9e6e1;
    --ink-black: #0b0c10;
    --navy-deep: #141b2c;
    --navy-mid: #26324d;
    --pitch-green: #1b2a1f;
    --floodlight: #5b6f93;
    --brand-red: #e0242f;
    --brand-navy: #1d2f6f;
    --white: #ffffff;
  }
  * { margin: 0; padding: 0; box-sizing: border-box; }
  html, body { width: 1200px; height: 1200px; overflow: hidden; }
  body {
    background: var(--stage);
    font-family: "Archivo Black", "Arial Black", sans-serif;
    color: var(--white);
  }
  .spread {
    position: absolute;
    left: 70px; top: 225px;
    width: 1060px; height: 750px;
    display: flex;
    box-shadow: 0 18px 40px rgba(0,0,0,.25);
  }
  .page {
    position: relative;
    width: 530px; height: 750px;
    overflow: hidden;
    background: var(--ink-black);
  }
  .page__photo {
    position: absolute; inset: 0;
  }
  .back-cover .page__photo {
    background:
      radial-gradient(ellipse at 45% 30%, rgba(91,111,147,.45), transparent 60%),
      linear-gradient(180deg, var(--navy-mid) 0%, var(--navy-deep) 45%, var(--ink-black) 100%);
    opacity: .85;
  }
  .front-cover .page__photo {
    background:
      radial-gradient(circle at 85% 8%, rgba(200,215,240,.55), transparent 22%),
      radial-gradient(ellipse at 65% 40%, rgba(120,40,50,.45), transparent 45%),
      linear-gradient(180deg, var(--navy-mid) 0%, var(--navy-deep) 35%, var(--pitch-green) 60%, var(--ink-black) 78%);
  }
  .event-mark {
    position: absolute;
    display: flex; align-items: center; gap: 10px;
    font-family: "Archivo Black", "Arial Black", sans-serif;
    font-size: 19px; line-height: 1.05;
    color: var(--white);
    text-transform: uppercase;
  }
  .event-mark__dot {
    width: 34px; height: 34px; border-radius: 50%;
    background: var(--brand-red); flex: none;
  }
  .front-cover .event-mark { left: 50px; top: 110px; width: 220px; }
  .back-cover .event-mark { left: 175px; top: 560px; width: 220px; }

  .back-cover__copy {
    position: absolute; left: 60px; right: 60px; top: 330px;
    text-align: center;
    font-size: 17px; line-height: 1.55;
    text-transform: uppercase;
  }
  .back-cover__email {
    position: absolute; left: 0; right: 0; top: 470px;
    text-align: center;
    font-size: 19px;
    color: var(--brand-red);
  }
  .front-cover__titles {
    position: absolute; left: 0; right: 0; top: 490px;
    text-align: center;
  }
  .front-cover__year {
    font-size: 58px; line-height: 1; letter-spacing: 1px;
  }
  .front-cover__name {
    margin-top: 8px;
    font-family: "Oswald", "Arial Narrow", sans-serif; font-weight: 500;
    font-size: 24px; color: var(--brand-red); text-transform: uppercase;
  }
  .front-cover__venue {
    margin-top: 4px;
    font-family: "Oswald", "Arial Narrow", sans-serif; font-weight: 500;
    font-size: 28px; text-transform: uppercase;
  }
  .front-cover__dates {
    margin-top: 10px; font-size: 15px; text-transform: uppercase;
  }
</style>
</head>
<body>
  <main class="spread">
    <section class="page back-cover">
      <div class="page__photo" role="img" aria-label="Dark photo of a junior rugby team huddled together in matching jerseys"></div>
      <p class="back-cover__copy">Please contact us to receive a tailored quote for your team for the Pacific Youth Rugby Cup.</p>
      <p class="back-cover__email">info@pacificyouthrugbycup.com</p>
      <div class="event-mark"><span class="event-mark__dot"></span><span>Pacific Youth Rugby Cup</span></div>
    </section>
    <section class="page front-cover">
      <div class="page__photo" role="img" aria-label="Two junior rugby players in a tackle under stadium floodlights with lightning in the night sky"></div>
      <div class="event-mark"><span class="event-mark__dot"></span><span>Pacific Youth Rugby Cup</span></div>
      <div class="front-cover__titles">
        <h1 class="front-cover__year">2019 PACIFIC</h1>
        <p class="front-cover__name">Youth Rugby Cup Invitational</p>
        <p class="front-cover__venue">Fukuoka, Japan</p>
        <p class="front-cover__dates">30th September to 4th October 2019</p>
      </div>
    </section>
  </main>
</body>
</html>
```